Vegan Jerky company needs a label for it's pouch, and a new logo

Dear Designers - this used to be a guaranteed project, however, due to the low quality of designs I have received, I have removed the guaranteed status. However, we need this product made and we will pay for a great, high quality design that meets the requirements of our brief.

We need sticker labels that will go onto the front and back of our vegan jerky package. Our package is a zip-sealable pouch, and we will either go with black, white or brown for the color of the pouch.

We need the concept, artwork, theme and logo designed. Pls choose the colors.

There will be four flavors. These can be finished as part of another project. The flavors are: Smoked Maple, Cracked Pepper, Teriyaki Sriracha, Original.

We are Lonny and Perla's Vegan Jerky.

Our food is vegan, non GMO, straight from the farm, organic, healthy, pure, clean, made in small batches and earth friendly. We use no chemicals or artificial flavors and our product is 100% natural.

Our kitchen is yours.

Target Market(s)

Vegetarians, vegans, health conscious, ecological, intelligent, caring.

Industry/Entity Type

Food Production

Logo Text

"Lonny and Perla" and "Our Kitchen is Yours"

Colors

Designer to choose colors to be used in the design.

Requirements
Must have
• earth friendly design, classy, hipster, vegan design, shabby chic,
Nice to have
• i have no ideas really...
• We prefer black and while, with a little splash of color. The last file is an idea I had but please use your own vision.

```html
<!DOCTYPE html>
<html lang="en">
<head>
<meta charset="utf-8">
<title>Lonny &amp; Perla's Vegan Jerky – Pouch Labels</title>
<link rel="stylesheet" href="https://fonts.googleapis.com/css2?family=Amatic+SC:wght@400;700&family=Kaushan+Script&family=Arimo:wght@400;700&display=swap">
<style>
  :root {
    --ink: #3c3c3b;
    --sage: #a7b49c;
    --leaf: #6f8f5f;
    --paper: #ffffff;
    --rule: #c8c8c8;
    --row: #e4e6e2;
    --caption: #111111;
    --display: "Amatic SC", "Arial Narrow", sans-serif;
    --script: "Kaushan Script", cursive;
    --body: "Arimo", Arial, sans-serif;
  }
  * { box-sizing: border-box; margin: 0; padding: 0; }
  html, body { width: 1200px; height: 1000px; overflow: hidden; background: var(--paper); }
  .board { position: relative; width: 1200px; height: 1000px; color: var(--ink); font-family: var(--body); }
  .abs { position: absolute; }

  .label { position: absolute; background: var(--paper); border: 1px solid var(--rule); overflow: hidden; }
  .label--front { left: 104px; top: 142px; width: 449px; height: 715px; }
  .label--back { left: 647px; top: 294px; width: 449px; height: 563px; }

  .brand-seal { position: absolute; border-radius: 50%; background: var(--ink); display: flex; align-items: center; justify-content: center; text-align: center; color: var(--paper); font-family: var(--display); font-weight: 700; line-height: .9; }

  .front-top { position: absolute; left: 0; top: 0; width: 100%; height: 213px; background: var(--sage); }
  .front-top .brand-seal { left: 163px; top: 54px; width: 124px; height: 124px; font-size: 30px; }
  .product-name { position: absolute; left: 0; top: 222px; width: 100%; text-align: center; font-family: var(--display); font-size: 80px; font-weight: 400; letter-spacing: 2px; line-height: 1; }
  .wave { position: absolute; left: 0; }

  .d { position: absolute; font-family: var(--display); font-weight: 700; line-height: .85; white-space: nowrap; }
  .s { position: absolute; font-family: var(--script); line-height: 1; white-space: nowrap; }
  .squeeze { transform-origin: left top; }

  .flavor-tag { left: 61px; top: 341px; width: 106px; height: 125px; }
  .flavor-tag .d { left: 5px; top: 26px; width: 98px; color: var(--paper); font-weight: 400; font-size: 40px; line-height: 1.1; }
  .no-chem { left: 61px; top: 510px; width: 53px; height: 166px; background: var(--ink); }
  .no-chem .inner { position: absolute; left: 50%; top: 50%; width: 160px; transform: translate(-50%,-50%) rotate(-90deg); display: flex; align-items: center; gap: 4px; color: var(--paper); font-family: var(--display); font-weight: 700; }
  .no-chem .big { font-size: 48px; line-height: 1; }
  .no-chem .small { font-size: 18px; line-height: .95; }
  .heart { left: 291px; top: 513px; width: 96px; height: 82px; }
  .heart .d { left: 0; top: 28px; width: 96px; text-align: center; color: var(--paper); font-size: 17px; line-height: .95; }

  .about { right: 240px; top: 20px; text-align: right; font-family: var(--display); font-size: 52px; font-weight: 400; line-height: .95; }
  .about-copy { right: 240px; top: 235px; width: 165px; text-align: right; font-size: 10.5px; line-height: 14px; }
  .about-copy p + p { margin-top: 11px; }
  .back-seal { left: 133px; top: 466px; width: 80px; height: 80px; font-size: 20px; }
  .weight { left: 40px; top: 533px; font-weight: 700; font-size: 16px; }

  .back-panel { position: absolute; left: 221px; top: 0; width: 228px; height: 100%; background: var(--ink); color: var(--paper); }
  .ingredients { left: 16px; top: 24px; width: 184px; font-size: 10.5px; line-height: 14px; }
  .facts { left: 16px; top: 102px; width: 168px; height: 190px; background: var(--paper); color: var(--ink); padding: 6px 8px; transform: rotate(-.6deg); font-size: 7px; }
  .facts h3 { font-size: 8px; font-weight: 700; letter-spacing: .3px; padding-bottom: 4px; border-bottom: 1px solid var(--ink); margin-bottom: 6px; }
  .facts .row { display: flex; justify-content: space-between; font-weight: 700; line-height: 11px; padding: 0 2px; }
  .facts .row.shade { background: var(--row); }
  .facts .row.sub { padding-left: 8px; }
  .facts .gap { border-top: 1px solid var(--ink); margin: 4px 0; }
  .facts .note { font-weight: 400; line-height: 9px; margin-top: 4px; border-top: 1px solid var(--ink); padding-top: 3px; }
  .whats-in { left: 18px; top: 316px; font-family: var(--display); font-size: 50px; font-weight: 400; line-height: 1; }
  .best-before { left: 16px; top: 536px; font-size: 14px; display: flex; align-items: center; gap: 8px; }
  .best-before .date { background: var(--paper); color: var(--ink); padding: 1px 6px; font-size: 13px; }

  .caption { position: absolute; top: 926px; font-weight: 700; font-size: 24px; color: var(--caption); }
  .caption-rule { position: absolute; top: 964px; height: 1px; background: #9a9a9a; }
</style>
</head>
<body>
<main class="board">

  <section class="label label--front" aria-label="Front label">
    <div class="front-top">
      <div class="brand-seal" aria-label="Lonny and Perla's">Lonny &amp;<br>Perla's</div>
    </div>
    <svg class="wave" style="top:208px" width="449" height="10" viewBox="0 0 449 10"><path d="M0 6 C120 2 300 9 449 4" fill="none" stroke="#3c3c3b" stroke-width="1.5"/></svg>
    <h1 class="product-name">VEGAN JERKY</h1>
    <svg class="wave" style="top:296px" width="449" height="14" viewBox="0 0 449 14"><path d="M0 3 C60 10 140 12 240 9 C320 7 400 6 449 7" fill="none" stroke="#3c3c3b" stroke-width="1.5"/></svg>

    <div class="abs flavor-tag">
      <svg width="106" height="125" viewBox="0 0 106 125"><path d="M0 15 H10 L10 0 L22 15 H106 V125 H0 Z" fill="#6f8f5f"/></svg>
      <span class="d">ORIGINAL<br>FLAVOR</span>
    </div>
    <span class="d" style="left:177px;top:360px;font-size:40px">HEALTHY</span>
    <span class="s" style="left:282px;top:342px;font-size:46px">pure</span>
    <span class="d" style="left:175px;top:402px;font-size:84px;font-weight:400">NON-GMO</span>
    <span class="d" style="left:63px;top:474px;font-size:40px;letter-spacing:2px">STRAIGHT FROM THE FARM</span>

    <div class="abs no-chem"><div class="inner"><span class="big">NO</span><span class="small">CHEMICALS OR<br>ARTIFICIAL FLAVORS</span></div></div>
    <span class="s" style="left:128px;top:500px;font-size:50px">organic</span>
    <span class="d squeeze" style="left:128px;top:552px;font-size:148px;font-weight:400;transform:scaleX(.6)">YUMMY</span>

    <div class="abs heart">
      <svg width="96" height="82" viewBox="0 0 96 82"><path d="M48 82 C20 60 0 44 0 24 C0 8 12 0 25 0 C36 0 44 7 48 15 C52 7 60 0 71 0 C84 0 96 8 96 24 C96 44 76 60 48 82 Z" fill="#3c3c3b"/></svg>
      <span class="d">EARTH-<br>FRIENDLY</span>
    </div>
    <span class="d" style="left:296px;top:602px;font-size:40px;font-weight:700;line-height:.9">100%<br>NATURAL</span>
  </section>

  <section class="label label--back" aria-label="Back label">
    <h2 class="abs about">ABOUT<br>LONNY<br>&amp;<br>PERLA´S</h2>
    <div class="abs about-copy">
      <p>We are Lonny and Perla's. Cus quasped eos quam, qui optas di quiate eost eum illitis quiam, offictint, ullis dolupis quiatur, as molupta turibusa quia nis moloreris estiost.</p>
      <p>Moffictint, ullis dolupis quiatur, as molupta turibusa quia nis moloreris estiost, corrum, core, aut invendam fugitatius dolut faceresto tet que plit la doluptam.</p>
      <p>Our kitchen is yours.</p>
    </div>
    <svg class="wave" style="top:514px" width="221" height="10" viewBox="0 0 221 10"><path d="M0 7 C70 3 150 4 221 3" fill="none" stroke="#3c3c3b" stroke-width="1.5"/></svg>
    <div class="brand-seal back-seal" aria-label="Lonny and Perla's">Lonny &amp;<br>Perla's</div>
    <span class="abs weight">000g ℮</span>

    <div class="back-panel">
      <p class="abs ingredients">Ingredients:<br>Icimusae (64%), sunduntum qua ligae (20%), voluptae porem (8%), sitas, at re etur, voles, restium, evendisquam - and nothing else!</p>
      <div class="abs facts">
        <h3>NUTRITION FACTS</h3>
        <div class="row"><span>Serving Size</span><span>...g</span></div>
        <div class="row"><span>Servings per Bag</span><span>...g</span></div>
        <div class="gap"></div>
        <div class="row"><span>Calories ...</span><span>...%</span></div>
        <div class="row shade"><span>Total Fat ... g</span><span>...%</span></div>
        <div class="row sub"><span>Saturated Fat ... g</span><span>...%</span></div>
        <div class="row shade"><span>Cholesterol ... mg</span><span>...%</span></div>
        <div class="row"><span>Sodium ... mg</span><span>...%</span></div>
        <div class="row shade"><span>Total Carb ... g</span><span>...%</span></div>
        <div class="row sub"><span>Dietary Fiber ... g</span><span>...%</span></div>
        <div class="row sub shade"><span>Sugars ... g</span><span>...%</span></div>
        <div class="row"><span>Protein ...G</span><span>...%</span></div>
        <p class="note">* Percent Daily Values are based on a 2,000 calorie diet.</p>
      </div>
      <h2 class="abs whats-in">WHAT´S<br>IN<br>THIS<br>BAG?</h2>
      <svg class="wave" style="top:520px" width="228" height="8" viewBox="0 0 228 8"><path d="M0 5 C80 2 160 3 228 2" fill="none" stroke="#ffffff" stroke-width="1.5"/></svg>
      <div class="abs best-before"><span>best before:</span><span class="date">01.01.2099</span></div>
    </div>
  </section>

  <p class="caption" style="left:104px">Front Label</p>
  <div class="caption-rule" style="left:0;width:285px"></div>
  <p class="caption" style="left:958px">Back Label</p>
  <div class="caption-rule" style="left:927px;width:273px"></div>

</main>
</body>
</html>
```